Maple Bug Guard Business Cards

A modern business card with a predominantly white background and a sleek design featuring Maple with complimentary greys or blacks to convey a professional and contemporary look.

Front:
Primarily white background. Limited use of company purple color can be neighbored by greys.
Text: Name, Title, Cell Phone, Office Phone, Website, email address

Back:
Background Continuation: The back of the card maintains the white background for consistency.
Company name “Maple” in company color and font, “Bug Guard” underneath or underneath left justified of “Maple.”
A subtle pattern or texture in shades of grey to add depth behind the company Logo in font.

logo color: hex #6212ab
font: antique olive nord D Regular

```html
<!DOCTYPE html>
<html lang="en">
<head>
<meta charset="utf-8">
<title>Maple Bug Guard – Business Card</title>
<link rel="stylesheet" href="https://fonts.googleapis.com/css2?family=Barlow+Condensed:wght@400;700&display=swap">
<style>
  :root {
    --card-bg: #f3f3f3;
    --name-ink: #3a3b3c;
    --title-purple: #7d3b9b;
    --brand-purple: #62369a;
    --contact-grey: #7f8084;
  }
  * { margin: 0; padding: 0; box-sizing: border-box; }
  html, body {
    width: 1200px;
    height: 720px;
    overflow: hidden;
    background: var(--card-bg);
  }
  .card {
    position: relative;
    width: 1200px;
    height: 720px;
    background: var(--card-bg);
    font-family: "Barlow Condensed", "Arial Narrow", sans-serif;
  }
  .identity {
    position: absolute;
    left: 118px;
    top: 122px;
  }
  .identity__name {
    font-size: 61px;
    font-weight: 400;
    line-height: 62px;
    letter-spacing: 0.5px;
    color: var(--name-ink);
    text-transform: uppercase;
  }
  .identity__title {
    font-size: 41px;
    font-weight: 400;
    line-height: 44px;
    color: var(--title-purple);
    text-transform: uppercase;
  }
  .contact {
    position: absolute;
    left: 117px;
    color: var(--contact-grey);
    font-size: 38px;
    line-height: 41px;
    font-weight: 400;
    list-style: none;
  }
  .contact--phones { top: 407px; }
  .contact--online { top: 525px; }
  .brand-name {
    position: absolute;
    right: 113px;
    top: 104px;
    font-size: 78px;
    line-height: 90px;
    font-weight: 700;
    letter-spacing: 6px;
    color: var(--brand-purple);
    text-transform: uppercase;
  }
</style>
</head>
<body>
  <main class="card">
    <header class="identity">
      <h1 class="identity__name">Daniel Reed</h1>
      <p class="identity__title">Director</p>
    </header>

    <ul class="contact contact--phones">
      <li>+61 355 210 4872</li>
      <li>0640 21 83 90</li>
    </ul>

    <ul class="contact contact--online">
      <li>www.maplebugguard.com</li>
      <li>hello@maplebugguard.com</li>
    </ul>

    <p class="brand-name">Maple</p>
  </main>
</body>
</html>
```